Marrowick Off-Grid Energy

The company provides world wide installations and products for off-grid energy solutions. This means AC power where there is no network available. Mostly this is with solar panels combined with hybrid inverters and Lithium batteries. In the future small windmills and hydropower. The company is Dutch but has a hub in Hungary to supply the Balkan and surrounding countries.

We sell all Tovu products and also Pyramoxa and Quillbrook energy products

I have 3 versions of my logo. 2 attached and the third is the Off-grid energy text in black. Just see what works best with the design.
Obviously I need a good design but also good coding. It needs to meet al the latest (Google) search engine standards and should heave a web shop.
The web shop should be able to work with different currencies and calculate international shipping fees. Orders should be paid with; credit card, Coinwisp, Faxo or whatever is used internationally.

Coding

Coded - Design and coding required

Number of Pages Required

5+ page

Font styles to use
Other font styles liked:
• see logo

Colors
0054AA
0677BA
7BADD7
CADEEF
E8F1F8
0094D4
00A9DD
6FCCEA
C7EBF8
E9F6FB
59FF00
82FF00
B8FF75
E3FFCB
F4FFEA
EB3D1F
EC4F4E
F09395
F8D3D4
FCEDEE

Requirements
Must have
• web shop
Nice to have
• slick design
Should not have
• stupid things ;-)

```html
<!DOCTYPE html>
<html lang="en">
<head>
<meta charset="utf-8">
<title>Marrowick Off-Grid Energy</title>
<link rel="stylesheet" href="https://fonts.googleapis.com/css2?family=Orbitron:wght@500;700&family=Montserrat:wght@400;500;600;700&display=swap">
<style>
:root{
  --orange:#f5461b;
  --orange-dark:#eb3d1f;
  --green:#82ff00;
  --green-soft:#a6fa64;
  --ink:#111;
  --grey:#8a8a8a;
  --sky:#dcebf7;
  --footer:#222;
  --white:#fff;
}
*{box-sizing:border-box;margin:0;padding:0}
html,body{width:1200px;height:3801px;overflow:hidden}
body{position:relative;background:var(--white);font-family:"Montserrat",sans-serif;color:var(--ink)}
.abs{position:absolute}
.display{font-family:"Orbitron",sans-serif;font-weight:500;letter-spacing:2px;text-transform:uppercase}
.ph{display:block}
.btn-grad{background:linear-gradient(90deg,var(--orange) 0%,#ff6a10 55%,var(--green-soft) 100%);color:#fff;border-radius:24px;font-weight:600;font-size:14px;display:flex;align-items:center;justify-content:center;gap:8px}

/* header */
.topline{left:0;top:0;width:1200px;height:3px;background:var(--orange)}
.brand{display:flex;align-items:center;gap:10px;font-family:"Montserrat",sans-serif;font-weight:700;font-size:30px;color:var(--ink)}
.brand-mark{width:26px;height:26px;background:var(--green)}
.nav{left:330px;top:38px;display:flex;gap:28px;font-family:"Orbitron",sans-serif;font-size:15px;letter-spacing:1px}
.nav .active{color:var(--orange)}
.call{left:905px;top:0;width:190px;height:88px}
.call-tab{left:0;top:0;width:42px;height:88px;background:linear-gradient(180deg,var(--green-soft),var(--orange));border-radius:0 0 22px 22px}
.call-icon{left:5px;top:46px;width:32px;height:32px;border-radius:50%;background:#fff;display:flex;align-items:center;justify-content:center}
.lang{left:117px;top:8px;width:60px;height:22px;border:1px solid #ddd;border-radius:12px;font-size:13px;display:flex;align-items:center;gap:5px;padding-left:4px}
.lang i{width:14px;height:14px;border-radius:50%;background:var(--orange);display:block}

/* hero */
.hero{left:0;top:130px;width:1200px;height:545px;background:linear-gradient(100deg,#6f7a6a 0%,#9c8f78 35%,#f2b263 62%,#f58c2c 75%,#6e6a3a 100%)}
.hero-title{left:0;top:172px;width:1200px;text-align:center;font-size:33px;line-height:44px;color:#111;letter-spacing:3px}
.hero-btn{left:515px;top:275px;width:168px;height:45px}
.arrow{width:48px;height:48px;border-radius:50%;background:#111;top:346px;display:flex;align-items:center;justify-content:center}
.tabs{left:160px;top:617px;width:880px;height:112px;background:#fff;border-radius:24px;box-shadow:0 6px 18px rgba(0,0,0,.12);display:flex;overflow:hidden}
.tab{flex:1;display:flex;flex-direction:column;align-items:center;justify-content:flex-end;padding-bottom:18px;gap:14px;font-weight:700;font-size:16px;border-left:1px solid #eee}
.tab.active{flex:0 0 208px;background:var(--orange);color:#fff;border:0}

/* about */
.about-glow{left:115px;top:860px;width:420px;height:400px;border-radius:50%;background:radial-gradient(#f1fbe6,rgba(255,255,255,0))}
.label{font-family:"Orbitron",sans-serif;font-size:17px;letter-spacing:2px;color:var(--orange);text-transform:uppercase}
.about-h{left:643px;top:896px;font-size:21px;line-height:30px;color:#111}
.about-p{left:643px;top:1003px;width:440px;font-size:15px;line-height:26px;color:var(--grey)}
.badge{left:392px;top:1159px;width:117px;height:122px;background:#111;border-radius:12px;color:#fff;text-align:center;padding-top:18px;font-weight:600;font-size:17px;line-height:25px}
.badge b{color:var(--orange);font-size:22px}

/* services */
.services{left:0;top:1429px;width:1200px;height:841px;background:linear-gradient(180deg,#e6f1fa,#cfe3f4)}
.panels{left:0;top:2105px;width:1200px;height:165px;background:linear-gradient(180deg,#6b8fc3,#1d3f82)}
.center{left:0;width:1200px;text-align:center}
.svc{top:1650px;width:316px;height:392px;background:#fff;padding:10px;text-align:center}
.svc.sel{border:2px solid var(--orange)}
.svc .ph{height:210px;border-radius:0 0 50% 50% / 0 0 40px 40px}
.svc h3{margin-top:16px;font-size:16px;line-height:22px;font-weight:500}
.svc p{margin-top:26px;font-size:13px;line-height:21px;color:var(--grey);padding:0 16px}

/* products */
.prod{top:2442px;width:240px;height:233px;border:1px solid #ccc;background:#fff}
.prod-name{top:2696px;font-size:17px;font-weight:500}
.prod-btns{top:2730px;display:flex;gap:6px}
.shop{width:114px;height:32px;font-size:14px;font-weight:500}
.cart{width:114px;height:32px;border:1px solid var(--orange);border-radius:16px;font-size:14px;display:flex;align-items:center;justify-content:center}

/* testimonials */
.testi{left:0;top:2866px;width:1200px;height:512px;background:var(--green-soft)}
.tcard{top:3050px;width:316px;height:200px;background:#fff;border-radius:22px;padding:16px 27px}
.stars{color:var(--orange);font-size:16px;letter-spacing:3px;display:flex;align-items:center;gap:6px}
.stars span{color:#555;font-size:13px;letter-spacing:0}
.tcard h4{margin-top:10px;font-size:16px;font-weight:600}
.tcard p{margin-top:10px;font-size:12px;line-height:17px;color:var(--grey)}
.author{margin-top:12px;display:flex;align-items:center;gap:12px;font-size:17px;color:#444}
.avatar{width:44px;height:44px;border-radius:50%;background:#9aa4ad}

/* footer */
.footer{left:0;top:3378px;width:1200px;height:423px;background:var(--footer);color:#fff}
.fcol h5{font-size:17px;font-weight:600;margin-bottom:22px}
.fcol ul{list-style:none;font-size:16px;line-height:30px}
.newsletter input{position:absolute;left:2px;top:85px;width:232px;height:38px;border:0;padding-left:16px;font-family:inherit;font-size:13px}
.newsletter .go{position:absolute;left:234px;top:85px;width:45px;height:38px;background:var(--orange);display:flex;align-items:center;justify-content:center}
.divider{left:111px;top:3718px;width:977px;height:1px;background:#888}
.pay{left:777px;top:3744px;display:flex;gap:5px}
.pay i{width:30px;height:20px;border-radius:3px;background:#dfe3ea;display:block}
</style>
</head>
<body>

<header>
  <div class="abs topline"></div>
  <a class="abs brand" style="left:110px;top:32px"><span class="brand-mark"></span>Marrowick</a>
  <nav class="abs nav">
    <span class="active">Home</span><span>About Us</span><span>Our Services</span><span>Shop</span><span>Contact Us</span>
  </nav>
  <div class="abs call">
    <div class="abs call-tab"></div>
    <div class="abs call-icon">
      <svg width="18" height="18" viewBox="0 0 24 24" fill="none" stroke="#f5461b" stroke-width="2"><path d="M22 16.9v3a2 2 0 0 1-2.2 2 19.8 19.8 0 0 1-8.6-3.1 19.5 19.5 0 0 1-6-6A19.8 19.8 0 0 1 2.1 4.2 2 2 0 0 1 4.1 2h3a2 2 0 0 1 2 1.7c.1 1 .4 1.9.7 2.8a2 2 0 0 1-.5 2.1L8 9.9a16 16 0 0 0 6 6l1.3-1.3a2 2 0 0 1 2.1-.4c.9.3 1.8.6 2.8.7a2 2 0 0 1 1.7 2z"/></svg>
    </div>
    <div class="abs" style="left:48px;top:32px;font-family:Orbitron,sans-serif;font-size:14px">Call Us:</div>
    <div class="abs" style="left:48px;top:56px;font-family:Orbitron,sans-serif;font-size:11px;letter-spacing:1px">(555)010 4477</div>
    <div class="abs lang"><i></i>EN</div>
  </div>
</header>

<section>
  <div class="abs hero ph" role="img" aria-label="House with rooftop solar panels and battery units at sunset"></div>
  <h1 class="abs hero-title display">Powering<br>the future anywhere</h1>
  <a class="abs hero-btn btn-grad">LEARN MORE <svg width="13" height="13" viewBox="0 0 16 16"><circle cx="8" cy="8" r="8" fill="#fff"/><path d="M6 4l4 4-4 4" stroke="#f5461b" stroke-width="2" fill="none"/></svg></a>
  <div class="abs arrow" style="left:34px"><svg width="16" height="16" viewBox="0 0 16 16"><path d="M11 2L5 8l6 6" stroke="#fff" stroke-width="2" fill="none"/></svg></div>
  <div class="abs arrow" style="left:1103px"><svg width="16" height="16" viewBox="0 0 16 16"><path d="M5 2l6 6-6 6" stroke="#fff" stroke-width="2" fill="none"/></svg></div>
  <div class="abs tabs">
    <div class="tab active">
      <svg width="46" height="46" viewBox="0 0 46 46" fill="none" stroke="#fff" stroke-width="2"><circle cx="22" cy="20" r="16"/><path d="M17 16a5 5 0 1 1 6 5v3"/><circle cx="23" cy="29" r="1" fill="#fff"/><path d="M10 32l-4 8 10-4"/></svg>
      Why Marrowick</div>
    <div class="tab">
      <svg width="42" height="40" viewBox="0 0 42 40" fill="none" stroke="#f5461b" stroke-width="1.6"><circle cx="21" cy="6" r="3"/><path d="M6 16h30l4 14H2z M14 16l-2 14 M28 16l2 14 M4 23h34 M21 30v8"/></svg>
      Solar Panels</div>
    <div class="tab">
      <svg width="52" height="42" viewBox="0 0 52 42" fill="none" stroke="#f5461b" stroke-width="1.6"><circle cx="8" cy="6" r="4" stroke="#82ff00"/><path d="M18 8h30l-4 16H14z M26 8l-3 16 M38 8l-3 16 M16 16h30"/><rect x="4" y="26" width="16" height="12"/><path d="M8 38v3 M16 38v3"/></svg>
      Hybrid Inverters</div>
    <div class="tab">
      <svg width="44" height="40" viewBox="0 0 44 40" fill="none" stroke="#f5461b" stroke-width="1.6"><rect x="2" y="8" width="40" height="30" rx="3"/><path d="M10 8V3h6v5 M28 8V3h6v5 M22 12l-4 8h6l-4 8"/></svg>
      Lithium Batteries</div>
  </div>
</section>

<section>
  <div class="abs about-glow"></div>
  <div class="abs ph" style="left:203px;top:822px;width:169px;height:181px;border-radius:10px;background:linear-gradient(180deg,#8cc0e8,#2c5c9e)" role="img" aria-label="Technician installing solar panels on a roof"></div>
  <div class="abs ph" style="left:392px;top:902px;width:183px;height:241px;border-radius:10px;background:linear-gradient(180deg,#4e6a8a,#d9a56a 45%,#2a2f35 60%,#6e9a4c)" role="img" aria-label="Containerised battery storage units at dusk"></div>
  <div class="abs ph" style="left:111px;top:1021px;width:260px;height:284px;border-radius:10px;background:linear-gradient(120deg,#d8c7a8,#8d7e6a 50%,#4d5a60)" role="img" aria-label="Wall-mounted inverter and battery system beside a house"></div>
  <div class="abs badge"><b>15 +</b><br>Years of<br>Experience</div>
  <div class="abs label" style="left:643px;top:860px">About Us</div>
  <h2 class="abs about-h display">Your expertise in<br>providing renewable<br>off-grid energy.</h2>
  <p class="abs about-p">Lorem ipsum dolor sit amet, consectetur adipiscing elit, sed do eiusmod tempor incididunt ut labore et dolore magna aliqua. Ut enim ad minim veniam, quis nostrud exercitation ullamco laboris nisi ut aliquip ex ea commodo consequat. Duis aute irure dolor in reprehenderit in voluptate velit esse cillum dolore eu fugiat nulla pariatur.</p>
  <a class="abs btn-grad" style="left:647px;top:1206px;width:168px;height:46px">LEARN MORE <svg width="13" height="13" viewBox="0 0 16 16"><circle cx="8" cy="8" r="8" fill="#fff"/><path d="M6 4l4 4-4 4" stroke="#f5461b" stroke-width="2" fill="none"/></svg></a>
</section>

<section>
  <div class="abs services"></div>
  <div class="abs panels ph" role="img" aria-label="Rows of blue solar panels"></div>
  <div class="abs center label" style="top:1498px">Our Services</div>
  <h2 class="abs center display" style="top:1535px;font-size:22px;line-height:31px">Why choose Marrowick<br>off-grid energy?</h2>
  <article class="abs svc" style="left:108px">
    <div class="ph" role="img" aria-label="Modern house with solar panel roof" style="background:linear-gradient(180deg,#4f86c9,#dfe8ee 55%,#6b8e4e)"></div>
    <h3 class="display">Custom off-grid<br>energy solutions</h3>
    <p>Lorem ipsum dolor sit amet, consectetur adipiscing elit, sed do eiusmod tempor incididunt ut labore</p>
  </article>
  <article class="abs svc sel" style="left:440px">
    <div class="ph" role="img" aria-label="Installer walking between rooftop solar panels" style="background:linear-gradient(180deg,#9fb8cf,#3a5f96 50%,#1f3d78)"></div>
    <h3 class="display">Product<br>installation</h3>
    <p>Lorem ipsum dolor sit amet, consectetur adipiscing elit, sed do eiusmod tempor incididunt ut labore</p>
  </article>
  <article class="abs svc" style="left:771px">
    <div class="ph" role="img" aria-label="Technician servicing solar panels on a roof" style="background:linear-gradient(180deg,#8aa6bc,#4a6a4a 35%,#3b4552)"></div>
    <h3 class="display">Maintenance<br>&amp; support</h3>
    <p>Lorem ipsum dolor sit amet, consectetur adipiscing elit, sed do eiusmod tempor incididunt ut labore</p>
  </article>
</section>

<section>
  <h2 class="abs display" style="left:108px;top:2372px;font-size:27px;font-weight:700;color:var(--orange);letter-spacing:4px">Our&nbsp; Products</h2>

  <div class="abs prod" style="left:108px"><div class="ph" role="img" aria-label="Two solar panels" style="margin:45px auto;width:150px;height:140px;background:linear-gradient(135deg,#3a5a9c,#1a2c5a)"></div></div>
  <div class="abs prod" style="left:355px"><div class="ph" role="img" aria-label="Hybrid inverter unit" style="margin:28px auto;width:140px;height:170px;border-radius:8px;background:linear-gradient(180deg,#f0f0f0,#bdbdbd 70%,#222)"></div></div>
  <div class="abs prod" style="left:601px"><div class="ph" role="img" aria-label="Lithium battery pack" style="margin:70px auto;width:190px;height:90px;border-radius:6px;background:linear-gradient(180deg,#555,#111)"></div></div>
  <div class="abs prod" style="left:848px"><div class="ph" role="img" aria-label="Wind turbine" style="margin:15px auto;width:110px;height:200px;background:linear-gradient(180deg,#e3eef6,#9fb6c8)"></div></div>

  <div class="abs prod-name" style="left:115px">Solar Panels</div>
  <div class="abs prod-name" style="left:362px">Hybrid Inverters</div>
  <div class="abs prod-name" style="left:608px">Lithium Batteries</div>
  <div class="abs prod-name" style="left:855px">Wind Turbines</div>

  <div class="abs prod-btns" style="left:111px"><a class="shop btn-grad">Shop Now</a><a class="cart">Add To Cart</a></div>
  <div class="abs prod-btns" style="left:358px"><a class="shop btn-grad">Shop Now</a><a class="cart">Add To Cart</a></div>
  <div class="abs prod-btns" style="left:604px"><a class="shop btn-grad">Shop Now</a><a class="cart">Add To Cart</a></div>
  <div class="abs prod-btns" style="left:851px"><a class="shop btn-grad">Shop Now</a><a class="cart">Add To Cart</a></div>
</section>

<section>
  <div class="abs testi"></div>
  <div class="abs center label" style="top:2948px;font-size:16px;text-transform:none">Testimonials</div>
  <h2 class="abs center display" style="top:2982px;font-size:23px">What our customers say</h2>
  <article class="abs tcard" style="left:111px">
    <div class="stars">★★★★★<span>03/02/2025</span></div>
    <h4>The Solar panel is great!</h4>
    <p>Lorem ipsum dolor sit amet, consectetur adipiscing elit, sed do eiusmod tempor incididunt</p>
    <div class="author"><span class="avatar" role="img" aria-label="Customer portrait"></span>Lena Vorst</div>
  </article>
  <article class="abs tcard" style="left:441px">
    <div class="stars">★★★★★<span>03/02/2025</span></div>
    <h4>The Solar panel is great!</h4>
    <p>Lorem ipsum dolor sit amet, consectetur adipiscing elit, sed do eiusmod tempor incididunt</p>
    <div class="author"><span class="avatar" role="img" aria-label="Customer portrait"></span>Lena Vorst</div>
  </article>
  <article class="abs tcard" style="left:771px">
    <div class="stars">★★★★★<span>03/02/2025</span></div>
    <h4>The Solar panel is great!</h4>
    <p>Lorem ipsum dolor sit amet, consectetur adipiscing elit, sed do eiusmod tempor incididunt</p>
    <div class="author"><span class="avatar" role="img" aria-label="Customer portrait"></span>Lena Vorst</div>
  </article>
</section>

<footer>
  <div class="abs footer"></div>
  <div class="abs brand" style="left:111px;top:3530px;color:#fff;font-size:36px"><span class="brand-mark"></span>Marrowick</div>
  <div class="abs fcol" style="left:401px;top:3437px;color:#fff">
    <h5>Shop</h5>
    <ul><li>Solar Panels</li><li>Hybrid Inverters</li><li>Lithium Batteries</li><li>Wind Turbines</li><li>(once available)</li><li>Hydropower</li></ul>
  </div>
  <div class="abs fcol" style="left:614px;top:3437px;color:#fff">
    <h5>Help Links</h5>
    <ul><li>Contact</li><li>Terms of us</li><li>Shipping Policy</li><li>Return Policy</li><li>Privacy Policy</li><li>Warranty</li><li>About Us</li></ul>
  </div>
  <div class="abs fcol newsletter" style="left:806px;top:3437px;width:290px;height:130px;color:#fff">
    <h5>Newsletter</h5>
    <p style="font-size:16px;line-height:25px;margin-top:-6px">Lorem ipsum dolor sit amet, consectetur adipiscing elit, sed do</p>
    <input type="email" placeholder="Enter your email">
    <a class="go"><svg width="20" height="12" viewBox="0 0 20 12"><path d="M0 6h17M12 1l5 5-5 5" stroke="#fff" stroke-width="2" fill="none"/></svg></a>
  </div>
  <div class="abs divider"></div>
  <div class="abs" style="left:113px;top:3744px;color:#fff;font-size:13px">Copyrights 2025 Company Name All Rights Reserved</div>
  <div class="abs pay" aria-label="Accepted payment methods"><i></i><i></i><i></i><i></i><i></i><i></i><i></i><i></i><i></i></div>
</footer>

</body>
</html>
```